Sign listing benefits of Wash and Fold Service

Sign 48 inches wide and 24 inches height to showcase service listed above.
Benefits include:
Saves Money
Saves Time
Convenient
Stain Treatment

Looking for something colorful (Blue and white are our business colors) the look of a laundromat business.

```html
<!DOCTYPE html>
<html lang="en">
<head>
<meta charset="utf-8">
<title>Wash &amp; Fold Services Sign</title>
<link href="https://fonts.googleapis.com/css2?family=Poppins:wght@600;700;800&display=swap" rel="stylesheet">
<style>
:root{
  --page:#a0a0a0;
  --navy:#0b1f3f;
  --royal:#1259d6;
  --band:#1f4f98;
  --white:#ffffff;
  --paper:#f4f7fb;
  --sky:#7cc6f2;
  --sea:#1d4f93;
  --divider:#d5dbe4;
}
*{margin:0;padding:0;box-sizing:border-box}
html,body{width:1200px;height:886px;overflow:hidden;background:var(--page);font-family:'Poppins',sans-serif}
.sign{position:absolute;left:30px;top:159px;width:1140px;height:568px;overflow:hidden;
  background:linear-gradient(180deg,var(--white) 0%,var(--paper) 60%,#e8eef6 100%);}
.water{position:absolute;left:0;top:0;width:1140px;height:568px}
.machine{position:absolute;left:728px;top:54px;width:300px;height:358px;border-radius:6px;
  background:linear-gradient(160deg,#fafbfc 0%,#e3e7ec 60%,#c9d0d8 100%)}
.laundry{position:absolute;left:826px;top:299px;width:314px;height:213px;border-radius:8px;
  background:linear-gradient(180deg,#e2c4b8 0%,#b9cdd6 30%,#6e93c6 50%,#e6e6ec 72%,#b4b6ba 100%)}
.kicker{position:absolute;left:63px;top:58px;font-size:25.5px;font-weight:700;color:var(--navy);letter-spacing:-.2px;white-space:nowrap}
.headline{position:absolute;left:61px;top:90px;font-size:60px;font-weight:800;color:var(--royal);letter-spacing:-.5px;white-space:nowrap;line-height:1.15}
.headline .amp{color:var(--navy);font-weight:600}
.benefits-band{position:absolute;left:63px;top:176px;width:666px;height:52px;background:var(--band);
  border-radius:10px 0 0 10px;box-shadow:0 8px 10px -6px rgba(11,31,63,.45);
  color:var(--white);font-size:28.5px;font-weight:700;line-height:52px;padding-left:28px;white-space:nowrap}
.benefit{position:absolute;top:252px}
.benefit-icon{width:56px;height:56px;border-radius:50%;background:var(--royal);border:3px solid var(--navy);
  box-shadow:inset 0 0 0 2px var(--white);display:flex;align-items:center;justify-content:center}
.benefit-label{margin-top:4px;font-size:25.5px;font-weight:700;color:var(--navy);line-height:.92}
.divider{position:absolute;top:262px;width:2px;height:95px;background:var(--divider)}
.contact-bar{position:absolute;left:0;top:450px;width:1140px;height:64px;background:var(--navy)}
.phone{position:absolute;left:63px;top:450px;height:64px;display:flex;align-items:center;gap:12px;
  color:var(--white);font-size:40px;font-weight:600;letter-spacing:-.3px}
.phone-icon{width:36px;height:36px;border-radius:50%;background:var(--white);display:flex;align-items:center;justify-content:center}
.bar-rule{position:absolute;left:385px;top:465px;width:2px;height:36px;background:var(--white)}
.web{position:absolute;left:418px;top:450px;line-height:64px;color:var(--white);font-size:26px;font-weight:700;letter-spacing:.6px}
.web .domain{color:#4aa3f0}
</style>
</head>
<body>
<div class="sign">
  <svg class="water" viewBox="0 0 1140 568" role="img" aria-label="Photo of splashing blue water with bubbles">
    <defs>
      <linearGradient id="wave" x1="0" y1="0" x2="0" y2="1">
        <stop offset="0" stop-color="#9bb6d6"/>
        <stop offset="1" stop-color="#1d4f93"/>
      </linearGradient>
      <linearGradient id="pool" x1="0" y1="0" x2="0" y2="1">
        <stop offset="0" stop-color="#5ab4ee"/>
        <stop offset="1" stop-color="#bfe6fb"/>
      </linearGradient>
    </defs>
    <path d="M0 395 C120 370 260 392 420 398 C600 405 720 360 860 300 C980 250 1060 215 1140 195 L1140 568 L0 568 Z" fill="url(#wave)" opacity=".85"/>
    <rect x="0" y="505" width="1140" height="63" fill="url(#pool)"/>
  </svg>
  <div class="machine" role="img" aria-label="Photo of a white front-loading washing machine"></div>

  <div class="kicker">ONE STOP DESTINATION FOR</div>
  <div class="headline">Wash <span class="amp">&amp;</span> Fold services</div>
  <div class="benefits-band">BENEFITS OF OUR WASH &amp; FOLD SERVICE</div>

  <div class="benefit" style="left:64px">
    <div class="benefit-icon">
      <svg width="30" height="30" viewBox="0 0 30 30"><circle cx="10" cy="9" r="6" fill="#fff"/><text x="10" y="12.5" font-size="9" font-weight="700" text-anchor="middle" fill="#1259d6" font-family="Poppins,sans-serif">$</text><ellipse cx="17" cy="20" rx="10" ry="7" fill="#fff"/></svg>
    </div>
    <div class="benefit-label">Saves<br>Money</div>
  </div>
  <div class="divider" style="left:172px"></div>
  <div class="benefit" style="left:201px">
    <div class="benefit-icon">
      <svg width="32" height="32" viewBox="0 0 32 32"><circle cx="16" cy="17" r="11" fill="none" stroke="#fff" stroke-width="3"/><path d="M16 11v6l4 3" stroke="#fff" stroke-width="2.5" fill="none" stroke-linecap="round"/><rect x="13" y="2" width="6" height="3" fill="#fff"/></svg>
    </div>
    <div class="benefit-label">Saves<br>Time</div>
  </div>
  <div class="divider" style="left:318px"></div>
  <div class="benefit" style="left:336px">
    <div class="benefit-icon">
      <svg width="30" height="30" viewBox="0 0 30 30"><path d="M14 6c3 0 4 4 7 4s4 4 1 6 1 6-3 6-5 2-8 0-6-3-4-7-1-9 3-9z" fill="#fff"/><circle cx="25" cy="6" r="2" fill="#fff"/><circle cx="5" cy="24" r="2" fill="#fff"/></svg>
    </div>
    <div class="benefit-label">Stain<br>Treatment</div>
  </div>
  <div class="divider" style="left:495px"></div>
  <div class="benefit" style="left:510px">
    <div class="benefit-icon">
      <svg width="32" height="32" viewBox="0 0 32 32"><path d="M14 14l4-9c2 0 3 2 2 5h7c2 0 2 3 1 4l-2 9c0 1-1 2-2 2h-10z" fill="#fff"/><circle cx="8" cy="22" r="6" fill="#fff"/><circle cx="8" cy="22" r="3" fill="#1259d6"/></svg>
    </div>
    <div class="benefit-label">Convenient</div>
  </div>

  <div class="contact-bar"></div>
  <div class="phone">
    <span class="phone-icon">
      <svg width="22" height="22" viewBox="0 0 24 24"><path d="M6.6 10.8c1.4 2.8 3.8 5.1 6.6 6.6l2.2-2.2c.3-.3.7-.4 1-.2 1.1.4 2.3.6 3.6.6.6 0 1 .4 1 1V20c0 .6-.4 1-1 1C10.6 21 3 13.4 3 4c0-.6.4-1 1-1h3.5c.6 0 1 .4 1 1 0 1.3.2 2.5.6 3.6.1.3 0 .7-.2 1z" fill="#1259d6"/></svg>
    </span>
    555.201.4488
  </div>
  <div class="bar-rule"></div>
  <div class="web">www.<span class="domain">brightrinselaundry</span>.com</div>

  <div class="laundry" role="img" aria-label="Photo of hands holding a stack of folded clean clothes"></div>
</div>
</body>
</html>
```